Beer Label/Realtor Promotion

I'm a Realtor in Vancouver, BC. I'm also a home brewer (of beer). As a gift to my clients, I'll be dropping off 3-6 750ml bottles of beer to their front door periodically. I'll need a label that will be used as a standard bottle label for all bottles, in addition to a neck sticker label that I'll adhere to the neck of the bottle. The neck sticker will be my contact info and real estate info, while the label needs to be something edgy and eye catching. I've included my business card, which may be useful for creative ideas and txt that will likely go on the label. I've included a picture of the pint glasses that were made for me in the past, personal photos of myself and my current business card. Feel free to leverage the design style on this glass as a basis for the design, or do something completely different. I've included a past design created for a magazine that may also be useful as a template.

Dimensions and label ideas can be found here:
http://www.brewmintly.com/post/oval-label-templates

A few ideas: This beer will be a pale ale. One idea was to name it or use the term "Open House Amber", maybe on a homequill for sale sign or something similar.

Another idea was to use personal photos of myself (which I've attached), one from the 90's and one from present day, using a caption like "Keeping your Real Estate and Beer needs in mind since the 90's"...or...Keeping it REAL Estate friendly since the 90's" or any other clever copy.

Target Market(s)

Targeting existing clients and potential real estate clients.

Industry/Entity Type

Real Estate

Requirements
Must have
• Edginess, creativity

```html
<!DOCTYPE html>
<html lang="en">
<head>
<meta charset="utf-8">
<title>Delgado Brewing Co. – Bottle and Neck Labels</title>
<link rel="stylesheet" href="https://fonts.googleapis.com/css2?family=Indie+Flower&family=Oswald:wght@400&family=Roboto+Condensed:wght@400;700&family=Kalam:wght@400&display=swap">
<style>
  :root {
    --canvas-bg: #f3f3f3;
    --canvas-edge: #d9d9d9;
    --label-bg: #2b2b2b;
    --label-bg-deep: #1f1f1f;
    --cream: #efe8d2;
    --neck-bg: #151515;
    --neck-text: #f1f1f1;
    --blue: #18b6dc;
    --red: #e3141b;
    --band-red: #b0141a;
  }
  * { box-sizing: border-box; margin: 0; padding: 0; }
  html, body { width: 1200px; height: 1000px; overflow: hidden; }
  body {
    background: radial-gradient(ellipse at center, #ffffff 0%, var(--canvas-bg) 60%, var(--canvas-edge) 100%);
    position: relative;
    font-family: "Roboto Condensed", sans-serif;
  }
  .label-set { position: absolute; top: 0; width: 240px; height: 1000px; }
  .label-set--blue { left: 283px; --accent: var(--blue); }
  .label-set--red { left: 670px; --accent: var(--red); }

  /* Neck sticker */
  .neck-label {
    position: absolute; left: 48px; top: 155px; width: 146px; height: 104px;
    background: var(--neck-bg);
    border-top: 3px solid var(--accent);
    border-bottom: 3px solid var(--accent);
    box-shadow: inset 0 5px 0 var(--neck-bg), inset 0 7px 0 var(--accent),
                inset 0 -5px 0 var(--neck-bg), inset 0 -7px 0 var(--accent);
    color: var(--neck-text);
    text-align: center;
    padding-top: 15px;
    white-space: nowrap;
  }
  .neck-label__name { font-family: "Oswald", sans-serif; font-size: 18px; letter-spacing: 2px; line-height: 23px; }
  .neck-label__line { font-size: 13px; line-height: 17px; letter-spacing: .3px; }
  .neck-label__line--email { font-size: 12px; }
  .neck-label__line--small { font-size: 11px; font-weight: 700; }

  /* Main label */
  .bottle-label {
    position: absolute; left: 3px; top: 478px; width: 234px; height: 292px;
    background: linear-gradient(180deg, var(--label-bg) 0%, var(--label-bg-deep) 100%);
    padding: 9px;
  }
  .bottle-label__frame {
    position: relative; width: 100%; height: 100%;
    border: 2px solid var(--cream);
  }
  .bottle-label__tagline {
    position: absolute; left: 10px; top: 6px;
    font-family: "Indie Flower", cursive; color: var(--cream);
    line-height: 17px; font-size: 14px;
  }
  .bottle-label__tagline strong { font-size: 17px; font-weight: 400; }
  .bottle-label__wordmark {
    position: absolute; left: 0; top: 46px; width: 212px;
    font-family: "Kalam", cursive; font-weight: 400;
    color: var(--accent); text-align: center;
  }
  .bottle-label__name { display: block; font-size: 38px; line-height: 40px; }
  .bottle-label__sub { display: block; font-size: 22px; line-height: 24px; }
  .bottle-label__since {
    position: absolute; left: 22px; top: 116px;
    font-family: "Indie Flower", cursive; color: var(--cream); font-size: 14px;
    line-height: 30px;
  }
  .bottle-label__since span { font-size: 26px; }
  .bottle-label__photos { position: absolute; left: 0; top: 150px; width: 212px; height: 122px; }
  .bottle-label__origin {
    position: absolute; left: 40px; top: 233px; width: 132px;
    text-align: center; color: var(--cream);
    font-family: "Kalam", cursive; font-size: 12px; line-height: 12px;
  }
  .bottle-label__origin b { font-weight: 400; font-size: 14px; display: block; line-height: 15px; }
</style>
</head>
<body>

<section class="label-set label-set--blue">
  <div class="neck-label">
    <p class="neck-label__name">REALTORMATEO</p>
    <p class="neck-label__line">CALL:(604) 555-0142</p>
    <p class="neck-label__line neck-label__line--email">mateo@realtormateo.com</p>
    <p class="neck-label__line neck-label__line--small">homequill Realty, Vancouver</p>
  </div>
  <article class="bottle-label">
    <div class="bottle-label__frame">
      <p class="bottle-label__tagline">Keeping it<br><strong>REAL Estate</strong> friendly</p>
      <h1 class="bottle-label__wordmark"><span class="bottle-label__name">Delgado</span><span class="bottle-label__sub">brewing co.</span></h1>
      <p class="bottle-label__since">since the <span>90's</span></p>
      <svg class="bottle-label__photos" viewBox="0 0 212 122">
        <defs>
          <linearGradient id="pastBlue" x1="0" y1="0" x2="1" y2="1"><stop offset="0" stop-color="#8a8a8a"/><stop offset="1" stop-color="#3e3e3e"/></linearGradient>
          <linearGradient id="nowBlue" x1="0" y1="0" x2="1" y2="1"><stop offset="0" stop-color="#8f7a68"/><stop offset="1" stop-color="#3d3f4c"/></linearGradient>
        </defs>
        <polygon role="img" aria-label="Black and white portrait of the realtor in the 1990s" points="0,0 100,0 92,28 104,44 98,80 0,80 0,122" fill="url(#pastBlue)"/>
        <polygon role="img" aria-label="Colour portrait of the realtor today" points="100,0 212,0 212,122 98,80 104,44 92,28" fill="url(#nowBlue)"/>
        <polyline points="100,0 92,28 104,44 98,80" fill="none" stroke="#18b6dc" stroke-width="3"/>
        <rect x="1" y="1" width="210" height="120" fill="none" stroke="#18b6dc" stroke-width="2"/>
        <polygon points="0,122 42,80 170,80 212,122" fill="#2b2b2b" stroke="#efe8d2" stroke-width="2"/>
      </svg>
      <p class="bottle-label__origin"><b>Brewed &amp; Bottled</b>East Vancouver, BC<br>2013</p>
    </div>
  </article>
</section>

<section class="label-set label-set--red">
  <div class="neck-label">
    <p class="neck-label__name">REALTORMATEO</p>
    <p class="neck-label__line">CALL:(604) 555-0142</p>
    <p class="neck-label__line neck-label__line--email">mateo@realtormateo.com</p>
    <p class="neck-label__line neck-label__line--small">homequill Realty, Vancouver</p>
  </div>
  <article class="bottle-label">
    <div class="bottle-label__frame">
      <p class="bottle-label__tagline">Keeping it<br><strong>REAL Estate</strong> friendly</p>
      <h1 class="bottle-label__wordmark"><span class="bottle-label__name">Delgado</span><span class="bottle-label__sub">brewing co.</span></h1>
      <p class="bottle-label__since">since the <span>90's</span></p>
      <svg class="bottle-label__photos" viewBox="0 0 212 122">
        <defs>
          <linearGradient id="pastRed" x1="0" y1="0" x2="1" y2="1"><stop offset="0" stop-color="#8a8a8a"/><stop offset="1" stop-color="#3e3e3e"/></linearGradient>
          <linearGradient id="nowRed" x1="0" y1="0" x2="1" y2="1"><stop offset="0" stop-color="#8f7a68"/><stop offset="1" stop-color="#3d3f4c"/></linearGradient>
        </defs>
        <polygon role="img" aria-label="Black and white portrait of the realtor in the 1990s" points="0,0 100,0 92,28 104,44 98,80 0,80 0,122" fill="url(#pastRed)"/>
        <polygon role="img" aria-label="Colour portrait of the realtor today" points="100,0 212,0 212,122 98,80 104,44 92,28" fill="url(#nowRed)"/>
        <polyline points="100,0 92,28 104,44 98,80" fill="none" stroke="#efe8d2" stroke-width="3"/>
        <polygon points="0,122 42,80 170,80 212,122" fill="#b0141a" stroke="#efe8d2" stroke-width="2"/>
      </svg>
      <p class="bottle-label__origin"><b>Brewed &amp; Bottled</b>East Vancouver, BC<br>2013</p>
    </div>
  </article>
</section>

</body>
</html>
```